Flyer for the Harvest of lanterns conference

Flyer design for an annual international conference called "VELMARK 2017". This is a conference for young adults, so we hope to produce a design that is both professional and appealing to young people in general

We'd like the flyer to showcase the conference brand logo, and clearly highlight the key information to people who will read it.

Target Market(s)

Young people, young adults

Industry/Entity Type

Religious

Font styles to use
Sans Serif

Colors

Designer to choose colors to be used in the design.

Requirements
Must have
• - Should be only one page (Vertical or Horizontal).
• - the VELMAK logo and all the information found in the attached text file. This includes: Main topic: Your sons and daughters shall prophesy,
• Dates and time, location, contact information and everything that is in the attached text file.
Nice to have
• It would be nice to see samples where the white logo is used and another where the black one is used.
Should not have
• This is NOT a folded flyer, we will be sticking it on doors and public places. And we will be printing large simple to put on walls. So only one page with few words like an add (the words are in the attached file)

```html
<!DOCTYPE html>
<html lang="en">
<head>
<meta charset="utf-8">
<title>VELMARK 2017 – Harvest of Lanterns Conference</title>
<link href="https://fonts.googleapis.com/css2?family=Oswald:wght@400;500;600;700&family=Lato:ital,wght@0,300;0,400;0,700;1,700;1,900&family=Roboto:wght@300;400&display=swap" rel="stylesheet">
<style>
  :root{
    --gold:#f0b21c;
    --gold-deep:#d98f08;
    --gold-light:#f7c94a;
    --ink:#2b2b2b;
    --grey-text:#3d3d3d;
    --panel:#dadada;
    --footer:#4f4f4f;
    --paper:#ffffff;
    --backdrop:#ecebe8;
  }
  *{margin:0;padding:0;box-sizing:border-box}
  html,body{width:1200px;height:1200px;overflow:hidden;background:var(--backdrop)}
  .flyer{
    position:absolute;left:180px;top:20px;width:735px;height:1015px;
    background:var(--paper);transform:scale(1.143);transform-origin:0 0;
    overflow:hidden;font-family:'Lato',sans-serif;color:var(--grey-text);
    box-shadow:0 6px 18px rgba(0,0,0,.15);
  }
  .flyer-shapes{position:absolute;left:0;top:0}
  .event-title{position:absolute;left:48px;top:36px;line-height:1}
  .event-title .name{display:block;font-family:'Lato',sans-serif;font-weight:400;font-size:42px;color:var(--ink);letter-spacing:1px}
  .event-title .year{display:block;font-family:'Oswald',sans-serif;font-weight:700;font-size:62px;color:var(--gold);margin-top:6px;margin-left:10px}
  .brand{position:absolute;left:0;width:735px;top:495px;display:flex;align-items:center;justify-content:center;gap:12px}
  .brand .dot{width:22px;height:22px;border-radius:50%;background:var(--gold)}
  .brand .word{font-family:'Lato',sans-serif;font-weight:700;font-size:30px;color:var(--ink);letter-spacing:4px}
  .theme{position:absolute;left:35px;top:572px;white-space:nowrap}
  .theme .lead{font-family:'Roboto',sans-serif;font-weight:300;font-size:32px;color:var(--ink);display:flex;align-items:flex-end;gap:6px;line-height:1.1}
  .theme .lead::after{content:"";width:255px;height:1px;background:#888;margin-bottom:7px}
  .theme .main{font-family:'Oswald',sans-serif;font-weight:500;font-size:38px;letter-spacing:-.3px;color:var(--gold);line-height:1.15;margin-top:2px}
  .theme .end{font-family:'Roboto',sans-serif;font-weight:400;font-size:42px;color:var(--ink);line-height:1.1}
  .schedule{
    position:absolute;left:28px;top:728px;width:312px;height:92px;border:2px solid #2a2a2a;border-radius:18px;
    background:linear-gradient(100deg,var(--gold-deep),var(--gold) 55%,var(--gold-light));padding:10px 12px;
    box-shadow:0 8px 10px -6px rgba(0,0,0,.35);white-space:nowrap;
  }
  .schedule .dates{font-family:'Oswald',sans-serif;font-weight:500;font-size:21px;letter-spacing:-.3px;color:#2a2a2a;line-height:1.3}
  .schedule .time{font-family:'Roboto',sans-serif;font-weight:400;font-size:27px;color:#fff;line-height:1.3;letter-spacing:.3px;margin-top:2px}
  .venue{position:absolute;top:848px;font-size:13.5px;line-height:17px;color:var(--grey-text)}
  .venue .label{font-weight:700;color:var(--gold-deep);font-size:13px;margin-bottom:6px}
  .venue.location{left:38px}
  .venue.room{left:282px}
  .venue-divider{position:absolute;left:246px;top:852px;width:2px;height:92px;background:var(--gold)}
  .conference{position:absolute;left:455px;top:572px;white-space:nowrap}
  .conference .lead{font-family:'Lato',sans-serif;font-size:30px;color:var(--gold-deep);line-height:1.05;letter-spacing:.5px}
  .conference .rest{font-family:'Oswald',sans-serif;font-weight:600;font-size:26px;color:var(--grey-text);line-height:1.3}
  .conference-rule{position:absolute;left:455px;top:658px;width:240px;height:3px;background:var(--gold)}
  .speakers-title{position:absolute;left:460px;top:680px;font-family:'Lato',sans-serif;font-style:italic;font-weight:900;font-size:24px;color:var(--gold)}
  .speakers{position:absolute;left:458px;top:718px;width:272px;height:237px;background:var(--panel);border-left:18px solid var(--gold);list-style:none}
  .speakers li{position:absolute;left:20px;font-size:11px;font-weight:700;color:#333;letter-spacing:.2px;white-space:nowrap}
  .speakers li::before{content:"";position:absolute;left:-20px;top:-1px;border-left:14px solid var(--gold);border-top:8px solid transparent;border-bottom:8px solid transparent}
  .footer{position:absolute;left:0;bottom:0;width:735px;height:60px;background:var(--footer);color:#fff;display:flex;align-items:center;justify-content:space-between;padding:0 32px 0 38px;font-size:14px;white-space:nowrap}
</style>
</head>
<body>
<main class="flyer">
  <svg class="flyer-shapes" width="735" height="1015" viewBox="0 0 735 1015">
    <defs>
      <linearGradient id="audience" x1="0" y1="0" x2="0.6" y2="1">
        <stop offset="0" stop-color="#e9e6df"/>
        <stop offset=".45" stop-color="#b59a84"/>
        <stop offset="1" stop-color="#5d4a42"/>
      </linearGradient>
      <linearGradient id="wingLeft" x1="0" y1="0" x2="1" y2="0">
        <stop offset="0" stop-color="#f4c23a"/>
        <stop offset="1" stop-color="#d98f08"/>
      </linearGradient>
      <linearGradient id="wingRight" x1="0" y1="0" x2="1" y2="0">
        <stop offset="0" stop-color="#f6c943"/>
        <stop offset="1" stop-color="#d98f08"/>
      </linearGradient>
    </defs>
    <rect x="0" y="0" width="735" height="420" fill="url(#audience)" role="img" aria-label="Photo of a seated audience listening to a speaker at a conference"/>
    <polygon points="0,300 230,410 390,398 0,545" fill="url(#wingLeft)"/>
    <polygon points="390,398 735,255 735,475 480,388" fill="url(#wingRight)"/>
    <polygon points="0,545 480,388 735,475 735,1015 0,1015" fill="#ffffff"/>
  </svg>

  <h1 class="event-title"><span class="name">VELMARK</span><span class="year">2017</span></h1>

  <div class="brand"><span class="dot"></span><span class="word">VELMAK</span></div>

  <section class="theme">
    <p class="lead">Your</p>
    <p class="main">SONS AND DAUGHTERS</p>
    <p class="end">Shall Prophesy</p>
  </section>

  <div class="schedule">
    <p class="dates">SEPTEMBER 1ST, 2ND &amp; 3RD 2017</p>
    <p class="time">START TIME: 6:00PM</p>
  </div>

  <div class="venue location">
    <p class="label">LOCATION:</p>
    <p>Lakeshore Pines Hotel<br>412 Harbor Road<br>Cedar Falls, ME 04999<br>United States</p>
  </div>
  <div class="venue-divider"></div>
  <div class="venue room">
    <p class="label">ROOM:</p>
    <p>Wildwood<br>Ballroom</p>
  </div>

  <section class="conference">
    <p class="lead">HARVEST OF</p>
    <p class="rest">LANTERNS CONFERENCE</p>
  </section>
  <div class="conference-rule"></div>

  <h2 class="speakers-title">Speakers</h2>
  <ul class="speakers">
    <li style="top:30px">PROPHET MARCEL ONDOUA</li>
    <li style="top:75px">BISHOP SAMUEL LUTETE</li>
    <li style="top:122px">PROPHET JOSEPH KIN MBUYI</li>
    <li style="top:162px">PROPHET ANDRE KOLELO</li>
    <li style="top:202px">PROPHET CALEB NTUMBA</li>
  </ul>

  <footer class="footer">
    <span>Tel:+1 (555) 014 2290</span>
    <span>Email:hello@velmakgathering.org</span>
    <span>Website: www.velmakevents.org</span>
  </footer>
</main>
</body>
</html>
```